Non-profit wants to save the world needs SiteBuilder presence

My name is Marco Estelani. I'm a photographer who started a charity (Rancho las Brisas) to help the rural schools and health clinics in Central America. We distribute schools supplies and help health clinics with much needed medical supplies and equipment. I need a way to accept donations. I need to have several different writers post to the blog (in Spanish and English). I have a domain name registered (www.rancholasbrisas.org) and started a simple wordpress site as well at http://www.rancholasbrisas.wordpress.com

Industry/Entity Type

Charity

```html
<!DOCTYPE html>
<html lang="en">
<head>
<meta charset="utf-8">
<title>Rancho las Brisas</title>
<link href="https://fonts.googleapis.com/css2?family=Open+Sans:wght@400;600;700&family=Arimo:wght@400;700&display=swap" rel="stylesheet">
<style>
:root{
  --page:#f2f2f2;
  --card:#ffffff;
  --ink:#333333;
  --muted:#777777;
  --soft:#999999;
  --rule:#e6e6e6;
  --nav:#2b2b2b;
  --accent:#2a8fcf;
  --footer:#333333;
  --footer-deep:#262626;
  --footer-text:#cfcfcf;
}
*{box-sizing:border-box;margin:0;padding:0}
html,body{width:700px;height:1200px;overflow:hidden}
body{background:var(--page);font-family:"Arimo",Arial,sans-serif;color:var(--ink);position:relative}
.abs{position:absolute}
.card{left:25px;top:30px;width:652px;height:848px;background:var(--card)}
.brand-mark{left:53px;top:58px;width:56px;height:56px;border-radius:50%;background:#7bb03a}
.brand-name{left:123px;top:68px;padding-left:7px;border-left:1px solid #ccc;font-size:8px;color:var(--muted);letter-spacing:.3px;text-transform:uppercase}
.contact{right:51px;top:61px;font-size:8px;color:var(--muted);display:flex;gap:8px;align-items:center;white-space:nowrap}
.contact span{display:flex;align-items:center;gap:5px}
.contact .sep{width:1px;height:10px;background:#ccc}
.search{left:534px;top:85px;width:115px;height:19px;background:#f3f3f3;font-size:7px;color:#aaa;font-style:italic;padding:5px 6px}
.search svg{position:absolute;right:7px;top:5px}
.nav{left:53px;top:127px;width:596px;height:33px;background:var(--nav);border-top:3px solid #bbb;display:flex}
.nav a{color:#fff;font:700 7.5px "Open Sans",sans-serif;text-decoration:none;padding:0 15px;line-height:30px;border-right:1px solid #3c3c3c;white-space:nowrap}
.nav a.active{background:#222;box-shadow:inset 0 2px 0 var(--accent);margin-top:-3px;line-height:36px}
.slide{left:53px;top:174px;width:596px;height:238px;background:linear-gradient(160deg,#3f6b2f,#6f8f4e 45%,#8a7a62 75%,#5d6a3f)}
.caption{left:53px;top:334px;width:336px;height:37px;background:rgba(20,20,20,.85);border-left:4px solid var(--accent);color:#fff;font:600 8.3px/11px "Open Sans",sans-serif;padding:13px 0 0 13px;white-space:nowrap}
.arrow{width:36px;height:36px;border-radius:50%;background:#222;top:278px}
.arrow svg{position:absolute;left:12px;top:11px}
.feature{top:447px;width:186px}
.feature h3{font:600 10.5px "Open Sans",sans-serif;margin-bottom:8px;white-space:nowrap}
.feature p{font-size:7.6px;line-height:12.5px;color:var(--muted)}
.rule{left:53px;width:596px;height:1px;background:var(--rule)}
.section-title{left:53px;font:600 10.5px "Open Sans",sans-serif}
.pager{top:552px;width:10px;height:10px;background:#ccc}
.project{top:574px;width:140px;height:110px;background:#f6f6f6;border-bottom:1px solid #e8e8e8}
.project .img{height:79px}
.project p{font:700 7.5px "Open Sans",sans-serif;text-align:center;margin-top:10px;white-space:nowrap}
.post{top:752px;width:140px;border-top:1px solid var(--rule);display:flex;gap:11px;padding-top:14px}
.post::before{content:"";position:absolute;left:0;top:-1px;width:20px;height:1px;background:var(--accent)}
.date{font-size:9px;color:var(--muted);width:28px;flex:none;line-height:13px}
.date b{display:block;font:600 14px "Open Sans",sans-serif;color:var(--ink);line-height:18px}
.post h4{font:400 10.5px "Open Sans",sans-serif;line-height:14px;color:var(--ink);margin-bottom:5px;white-space:nowrap}
.post p{font-size:7.4px;line-height:12px;color:var(--muted)}
.footer{left:25px;top:882px;width:652px;height:255px;background:var(--footer)}
.footer-bar{left:25px;top:1137px;width:652px;height:30px;background:var(--footer-deep);font-size:7px;color:#bbb;padding:11px 28px}
.fcol{top:914px;width:140px;color:var(--footer-text)}
.fcol h5{font:700 8.5px "Open Sans",sans-serif;color:#fff;padding-bottom:9px;border-bottom:1px solid #444;margin-bottom:11px}
.fcol p{font-size:7.3px;line-height:12.5px}
.fcol ul{list-style:none;font-size:7.5px}
.menu li{margin-bottom:27px}
.recent li{margin-bottom:11px;white-space:nowrap}
.recent i{display:block;color:#888;font-size:7px;margin-top:7px}
.social{left:510px;top:946px;width:167px;height:150px;background:#fff;border-bottom:1px solid #ddd}
.social .head{display:flex;gap:6px;padding:6px 5px}
.social .sq{width:32px;height:32px;background:#7bb03a}
.social .nm{font:700 8px Arial,sans-serif;color:#333}
.social .like{display:inline-block;margin-top:3px;background:#4c66a4;color:#fff;font:700 7px Arial,sans-serif;padding:2px 5px}
.social .count{font-size:6px;color:#888;border-top:1px solid #ccc;padding:3px 5px}
.social .count b{color:#333}
.faces{display:grid;grid-template-columns:repeat(5,30px);gap:3px;padding:2px 5px}
.faces div{height:32px}
.social .plug{font-size:6px;color:#333;padding:4px 5px;display:flex;gap:3px;align-items:center}
.social .plug span{width:7px;height:7px;background:#4c66a4;display:inline-block}
</style>
</head>
<body>
<div class="abs card"></div>

<header>
  <div class="abs brand-mark" aria-hidden="true"></div>
  <div class="abs brand-name">Rancho las Brisas</div>
  <div class="abs contact">
    <span><svg width="9" height="7" viewBox="0 0 9 7"><rect width="9" height="7" fill="#666"/><path d="M0 0l4.5 4L9 0" stroke="#fff" fill="none"/></svg>contact@rancholasbrisas.org</span>
    <i class="sep"></i>
    <span><svg width="8" height="8" viewBox="0 0 8 8"><circle cx="4" cy="2.2" r="2" fill="#666"/><path d="M0 8c0-3 8-3 8 0z" fill="#666"/></svg>call centre: 02 987 654 321</span>
  </div>
  <div class="abs search">Search...
    <svg width="9" height="9" viewBox="0 0 9 9"><circle cx="3.6" cy="3.6" r="2.8" stroke="#888" stroke-width="1.2" fill="none"/><path d="M5.6 5.6L8.5 8.5" stroke="#888" stroke-width="1.4"/></svg>
  </div>
  <nav class="abs nav">
    <a class="active" href="#">Home</a><a href="#">About</a><a href="#">Make a donation</a><a href="#">Contact</a>
  </nav>
</header>

<main>
  <div class="abs slide" role="img" aria-label="Photographer kneeling on a rural dirt path photographing two young girls, villagers walking among trees"></div>
  <div class="abs caption">Join Us to help the rural schools and health clinics in Central America.</div>
  <div class="abs arrow" style="left:34px"><svg width="12" height="14" viewBox="0 0 12 14"><path d="M8 2L3 7l5 5" stroke="#fff" stroke-width="2.4" fill="none"/></svg></div>
  <div class="abs arrow" style="left:631px"><svg width="12" height="14" viewBox="0 0 12 14"><path d="M4 2l5 5-5 5" stroke="#fff" stroke-width="2.4" fill="none"/></svg></div>

  <section>
    <div class="abs feature" style="left:53px"><h3>Lorem dolor sit</h3><p>Lorem ipsum dolor sit amet, consectetur adipiscing elit, sed do eiusmod tempor incididunt ut labore et dolore magna aliqua. Ut.</p></div>
    <div class="abs feature" style="left:256px"><h3>Lorem ipsum dolor sit</h3><p style="color:#333">Lorem ipsum dolor sit amet, consectetur adipiscing elit, sed do eiusmod tempor incididunt ut labore et dolore magna.</p></div>
    <div class="abs feature" style="left:459px"><h3>Lorem ipsum</h3><p>Lorem ipsum dolor sit amet, consectetur adipiscing elit, sed do eiusmod tempor incididunt ut labore et dolore magna aliqua. Ut.</p></div>
  </section>

  <div class="abs rule" style="top:528px"></div>
  <h2 class="abs section-title" style="top:551px">Recent Projects</h2>
  <div class="abs pager" style="left:625px"></div>
  <div class="abs pager" style="left:639px"></div>
  <div class="abs project" style="left:53px"><div class="img" role="img" aria-label="Photographer with children on a village path" style="background:linear-gradient(135deg,#4d7a3a,#8d8a70)"></div><p>Est laborum</p></div>
  <div class="abs project" style="left:205px"><div class="img" role="img" aria-label="Volunteer handing supplies to village children" style="background:linear-gradient(135deg,#9c9588,#6c5e4e)"></div><p>Lorem ipsumus</p></div>
  <div class="abs project" style="left:357px"><div class="img" role="img" aria-label="Two men standing in a supply shop" style="background:linear-gradient(135deg,#b8453f,#5a6e8a)"></div><p>Lorem ipsum dolor</p></div>
  <div class="abs project" style="left:509px"><div class="img" role="img" aria-label="Group of schoolchildren with balloons" style="background:linear-gradient(135deg,#c7a28a,#7a8a9a)"></div><p>Lorem ipsum</p></div>

  <div class="abs rule" style="top:707px"></div>
  <h2 class="abs section-title" style="top:730px">Recent Blog Posts</h2>
  <article class="abs post" style="left:53px"><div class="date"><b>14</b>Sep<br>2014</div><div><h4>Rancho las Brisas<br>Inaugural Brigade</h4><p style="color:#333">Starting a charity is a lot like grabbing.</p></div></article>
  <article class="abs post" style="left:205px"><div class="date"><b>14</b>Sep<br>2014</div><div><h4>Hello world!</h4><p>Welcome to SiteBuilder.<br>This is your first post. Edit or.</p></div></article>
  <article class="abs post" style="left:357px"><div class="date"><b>13</b>Sep<br>2014</div><div><h4>Lorem Ipsum</h4><p style="color:#333">Lorem ipsum dolor sit amet, consectetur adipiscing elit,.</p></div></article>
  <article class="abs post" style="left:509px"><div class="date"><b>12</b>Sep<br>2014</div><div><h4>Lorem ipsum dolor</h4><p style="color:#333">Lorem ipsum dolor sit amet, consectetur adipiscing elit,.</p></div></article>
</main>

<footer>
  <div class="abs footer"></div>
  <div class="abs fcol" style="left:53px"><h5>About</h5><p>We are help the rural schools and health clinics in Central America. We distribute schools supplies and help health clinics with much needed medical supplies and equipment. I need a way to accept donations. Join Us to help the rural schools and health clinics in Central America.</p></div>
  <div class="abs fcol" style="left:205px"><h5>Menu</h5><ul class="menu"><li>Home</li><li>About</li><li>Make a donation</li><li>Contact</li></ul></div>
  <div class="abs fcol" style="left:357px"><h5>Recent Posts</h5><ul class="recent"><li>Rancho las Brisas Inaugural Brigade<i>Sep 14, 2014</i></li><li>Hello world!<i>Sep 14, 2014</i></li><li>Lorem Ipsum<i>Sep 13, 2014</i></li></ul></div>
  <div class="abs fcol" style="left:509px"><h5>Follow Us</h5></div>
  <div class="abs social">
    <div class="head"><div class="sq" aria-hidden="true"></div><div><div class="nm">Rancho las Brisas</div><span class="like">Like</span></div></div>
    <div class="count">1,511 people like <b>Rancho las Brisas</b></div>
    <div class="faces" role="img" aria-label="Profile photos of supporters">
      <div style="background:#8a7d6e"></div><div style="background:#c9a98c"></div><div style="background:#6e5a4a"></div><div style="background:#3a3a3a"></div><div style="background:#7f8c7a"></div>
      <div style="background:#5a4a42"></div><div style="background:#a7b4c4"></div><div style="background:#c7b8a4"></div><div style="background:#d8a48a"></div><div style="background:#6a6a72"></div>
    </div>
    <div class="plug"><span></span>Social plugin</div>
  </div>
  <div class="abs footer-bar">Copyright © 2014. All Rights Reserved.</div>
</footer>
</body>
</html>
```